JMT - Business Card Design Project

We need a business card based on our logo
Updates

Hi I just upload logo file in AI format Thanks and regards

Target Market(s)

Bank, Big companies, Business owners

Industry/Entity Type

Business

Font styles to use
Sans Serif

```html
<!DOCTYPE html>
<html lang="en">
<head>
<meta charset="utf-8">
<title>JMT Business Card</title>
<link rel="stylesheet" href="https://fonts.googleapis.com/css2?family=Titillium+Web:wght@400&display=swap">
<style>
  :root {
    --navy: #1b2d55;
    --slate: #7e8d8f;
    --ink: #4d4f52;
    --paper: #ffffff;
    --backdrop: #eceef0;
  }
  * { margin: 0; padding: 0; box-sizing: border-box; }
  html, body {
    width: 1200px; height: 864px; overflow: hidden;
    background: var(--backdrop);
    font-family: "Titillium Web", sans-serif;
  }
  .card {
    position: absolute; left: 100px; top: 146px;
    width: 1000px; height: 572px;
    background: var(--paper);
    box-shadow: 0 6px 24px rgba(0,0,0,.12);
    overflow: hidden;
  }
  .brand {
    position: absolute; left: 78px; top: 200px;
    display: flex; align-items: center; gap: 18px;
  }
  .brand-square { width: 40px; height: 40px; background: var(--navy); flex: none; }
  .brand-name {
    font-size: 64px; font-weight: 400; line-height: 1;
    color: var(--navy); letter-spacing: 4px;
  }
  .rule { position: absolute; height: 3px; background: var(--navy); }
  .rule-left { left: 0; top: 330px; width: 510px; }
  .rule-right { left: 846px; top: 300px; width: 154px; }
  .person { position: absolute; left: 538px; top: 262px; }
  .person-name { font-size: 40px; font-weight: 400; color: var(--ink); line-height: 1.1; }
  .person-title { font-size: 21px; font-weight: 400; color: var(--ink); }
  .contacts { position: absolute; left: 540px; top: 380px; list-style: none; }
  .contacts li {
    display: flex; align-items: center; gap: 20px;
    font-size: 26px; color: var(--ink); height: 46px;
  }
  .contacts svg { width: 28px; height: 24px; fill: var(--slate); flex: none; }
  .address {
    position: absolute; left: 78px; top: 440px;
    font-size: 26px; color: var(--ink); line-height: 1.3;
  }
  .band { position: absolute; left: 0; bottom: 0; width: 100%; height: 28px; background: var(--navy); }
</style>
</head>
<body>
  <div class="card">
    <div class="brand">
      <span class="brand-square" aria-hidden="true"></span>
      <span class="brand-name">JMT</span>
    </div>

    <div class="rule rule-left"></div>
    <div class="rule rule-right"></div>

    <div class="person">
      <div class="person-name">Julien Marchand</div>
      <div class="person-title">Managing Director</div>
    </div>

    <ul class="contacts">
      <li>
        <svg viewBox="0 0 28 24" aria-hidden="true"><path d="M2 8c0-4 6-6 12-6s12 2 12 6v2h-6V7c-2-1-10-1-12 0v3H2zM7 11h14l3 11H4z"/></svg>
        0012 3456 789
      </li>
      <li>
        <svg viewBox="0 0 28 24" aria-hidden="true"><path d="M2 4h24v16H2zM4 6v1l10 7 10-7V6zm0 4v8h20v-8l-10 7z"/></svg>
        info@yourwebsite.com
      </li>
      <li>
        <svg viewBox="0 0 28 24" aria-hidden="true"><path d="M2 2h24v15H2zm3 3v9h18V5zM11 18h6v2h3v2H8v-2h3z"/></svg>
        www.yourwebsite.com
      </li>
    </ul>

    <div class="address">Your Adress Inc 00 2nd Lane<br>Ave Edison, NJ 00000</div>

    <div class="band"></div>
  </div>
</body>
</html>
```